Create a modern, visually appealing flyer for Courier Service.

Thornbury Freightworks Flyer Design Brief

Project Overview
Create a modern, visually appealing, front-and-back 8.5"x11" flyer for Thornbury Freightworks to distribute to potential customers and vendors. The flyer should emphasize the company's expansive service area, reliability, technological capabilities, and broad service offerings.

Flyer Goals
Showcase Thornbury's extensive regional coverage
Highlight core services, industries served, technology integration, certifications, and fleet capabilities
Convey reliability, modernity, and technology-driven professionalism
Encourage further interaction via a QR code (to be placed later by Thornbury)

Visual Style & Branding
Color Scheme: Creative, modern colors that are vibrant and appealing, suitable for a technology-driven and professional logistics company.
Font Selection: Modern, clean, professional fonts; readability is essential. Update to Logo
Design Aesthetic: Balanced mix of minimalistic/clean, tech-driven/futuristic, and sophisticated/professional elements.
Background: Incorporate abstract graphic patterns or imagery reflecting logistics, technology, or mapping concepts (e.g., subtle maps, abstract roads).

Content Layout

Front Side

Company Name & Logo: Prominent but balanced

Service Area Map: Modern, stylized graphic highlighting North Dakota, Minnesota, Montana, South Dakota, and Northern Iowa, clearly marking major cities within these areas

Vehicle Graphic: Stylized graphic featuring a Velkor Haulmate van with the Thornbury logo clearly visible

Certifications (as official logo badges): HIPAA, Hazmat/DOT, Radiopharmaceutical, TSA/IAC

Contact Information:

Thornbury Freightworks, LLC

4630 9th St S, Suite 215, Fargo, ND 58104

www.thrnbry-example.com | orders@thrnbry-example.com

Back Side

Core Services (icons, modern style):

STAT/ASAP

Same Day

Next Day

Scheduled

Extended Drives

Onboard Courier / Hand Carry

Reverse Logistics

White Glove

Warehousing

Industries Served (icons matching services style):

Healthcare & Life Sciences

Pharmaceuticals

Retailers & E-Commerce

Distributors & Manufacturers

Educational Institutions

Legal & Financial Services

Food & Beverage

Technology & IT Companies

Government & Defense Companies

Technology Highlights:

Advanced Integration Capabilities

GPS Tracking

Live Vehicle Monitoring

Client Online Portal

Emphasis on Real-Time Tracking and seamless integrations

Fleet Capabilities:

Variety of Vehicles: Sedans, SUVs, Pickup Trucks, Cargo Vans, Sprinters, Straight Trucks

Key Vehicle Features: Liftgate capabilities prominently noted

Hub Locations: Clearly listed:

Fargo, ND

Bismarck, ND

Devils Lake, ND

Grand Forks, ND

Airport Codes Serviced:

FAR - Fargo, ND

BIS - Bismarck, ND

MOT - Minot, ND

GFK - Grand Forks, ND

XWA - Williston, ND

DIK - Dickinson, ND

DVL - Devils Lake, ND

JMS - Jamestown, ND

ABR - Aberdeen, SD

ATY - Watertown, SD

TRF - Thief River Falls, MN

BJI - Bemidji, MN

DTL - Detroit Lakes, MN

MSP - Minneapolis/St. Paul, MN

Design Elements

Use of modern graphics and custom icons for services and industries

Abstract patterns or technology-driven imagery

Professional but approachable tone, using concise, bulleted text organized clearly in sections

Avoid event-specific language; design for long-term general use

Imagery

Stylized, consistent iconography for services and industries

Stylized vehicle graphics (Velkor Haulmate van)

Custom graphics illustrating technology integrations (if official graphics unavailable)

Images from software provider's website: www.PlexoviaSystems-example.com

Technical Requirements

8.5” x 11” flyer, double-sided

Digital-ready files provided for printing in-house; no specific print preferences necessary

High-resolution files suitable for both print and digital use

Deliverables

Editable source files (Adobe Illustrator, Photoshop, or InDesign)

High-resolution PDF for printing

Web-friendly PDF or digital version

This flyer should clearly communicate Thornbury Freightworks’ commitment to reliable, technology-enhanced logistics solutions across the region, effectively engaging diverse audiences across key industries.

Concept 1: Modern Technology Hub
Front:
Dominated by an abstract, vibrant map illustrating the service region with key cities pinpointed.
The Thornbury logo prominently at the top left, with stylized Velkor Haulmate van graphic subtly integrated onto the map roads.
Certifications as bold, minimalistic badges along the lower edge.
Crisp, clear contact info at bottom-right.
Back:
Split vertically into distinct sections, each clearly labeled with modern iconography for:
Core Services
Industries Served
Technology Highlights (with Plexovia Systems visuals)
Fleet Capabilities (vehicle silhouettes/icons)
Airport codes listed in a streamlined table format along the bottom.
Abstract tech-pattern background (faded nodes, routes, or circuit-board style).

Concept 2: Futuristic Minimalism
Front:
Sleek, minimalist layout with a clean white or very light background.
Modern service area map using minimalist outlines and dots for major cities, in gradient blues or tech-inspired palette.
Prominent Thornbury Freightworks logo at top-center.
Stylized Velkor Haulmate graphic appearing subtly at bottom corner.
Certifications displayed vertically as sleek, simplified logo badges.
Back:
Horizontally segmented sections for:
Core Services with clean, futuristic icons.
Industries Served section with matching sleek icons.
Technology Highlights, centered around Plexovia Systems graphics and abstract integrated circuit imagery.
Fleet Capabilities detailed with simplified vehicle graphics.
Clearly defined hub locations and airport codes in a clean, structured list along the side.

Concept 3: Bold & Vibrant Professionalism
Front:
Bright, vivid color blocking with abstract geometric shapes referencing routes and logistics paths.
The service map as a central graphic, bold and modern, clearly marking key hubs.
A prominent stylized Velkor Haulmate van with Thornbury logo creatively placed along the lower third of the flyer.
Certifications featured prominently within colored circular badges along the top or side.
Contact details neatly integrated at the bottom.
Back:
Dynamic grid layout clearly displaying:
Core Services and Industries Served with bold, vibrant icons.
Technology Highlights, clearly emphasized with screenshots or custom graphics from Plexovia Systems.
Fleet Capabilities section featuring colorful vehicle silhouettes/icons.
Hub locations and airport codes clearly called out within visually appealing graphics or charts.
Rich abstract graphical background elements maintaining professional readability.

Designers should not use AI for designs.

Target Market(s)

Businesses Needing Courier Services

Font styles to use
Sans Serif

```html
<!DOCTYPE html>
<html lang="en">
<head>
<meta charset="utf-8">
<title>Thornbury Freightworks – Core Services</title>
<link rel="stylesheet" href="https://fonts.googleapis.com/css2?family=Asap+Condensed:wght@700&family=Montserrat:wght@400;500;700&display=swap">
<style>
:root{
  --brown:#8b5e3c;
  --tan:#b8917a;
  --cream:#fffcf5;
  --white:#ffffff;
}
*{margin:0;padding:0;box-sizing:border-box}
html,body{width:848px;height:1200px;overflow:hidden;background:var(--cream)}
body{font-family:"Montserrat",sans-serif;color:var(--brown)}
.flyer{position:relative;width:848px;height:1200px;background:var(--cream)}
.abs{position:absolute}
.heading{font-family:"Asap Condensed",sans-serif;font-weight:700;line-height:1}

.header-band{left:0;top:0;width:848px;height:152px;background:var(--brown)}
.header-title{left:0;width:848px;top:58px;text-align:center;font-size:50px;color:var(--white)}

.service{position:absolute;width:150px;margin-left:-75px;text-align:center}
.service-icon{width:62px;height:62px;margin:0 auto;border-radius:12px;background:var(--brown);display:flex;align-items:center;justify-content:center}
.service-icon svg{width:40px;height:40px}
.service-label{font-weight:700;font-size:18px;white-space:nowrap;margin-top:12px;letter-spacing:.3px}
.divider{position:absolute;width:2px;background:var(--tan)}

.industries-pill{left:256px;top:419px;width:331px;height:60px;border-radius:14px;background:var(--tan);color:var(--white);font-size:35px;display:flex;align-items:center;justify-content:center}
.industry-list{position:absolute;list-style:none;font-size:21px;line-height:1.02}
.industry-list li{position:relative;padding-left:23px;margin-bottom:20px}
.industry-list li::before{content:"";position:absolute;left:-1px;top:2px;width:9px;height:9px;border-radius:50%;background:var(--tan)}

.tech-band{left:0;top:718px;width:848px;height:290px;background:var(--brown)}
.tech-title{left:46px;top:755px;font-size:30px;color:var(--white)}
.tech-list{position:absolute;left:46px;top:801px;list-style:none;color:var(--white);font-size:19.5px;line-height:1}
.tech-list li{position:relative;padding-left:25px;margin-bottom:11.5px}
.tech-list li::before{content:"";position:absolute;left:2px;top:7px;width:8px;height:8px;border-radius:50%;background:var(--white)}

.fleet-card{left:440px;top:751px;width:361px;height:228px;border-radius:26px;background:var(--white);padding:32px 20px 0 26px}
.fleet-title{font-size:25px;color:var(--brown)}
.fleet-text{font-size:16.5px;line-height:1.24;margin-top:9px;color:var(--brown)}
.fleet-card .second{margin-top:18px}
.fleet-card .liftgate{margin-left:-2px;margin-top:8px}

.hub-band{left:0;top:1008px;width:848px;height:192px;background:var(--tan);color:var(--white);text-align:center}
.hub-title{font-size:26px;margin-top:14px}
.hub-list{font-size:16.5px;margin-top:13px}
.airport-title{font-size:27px;margin-top:11px}
.airport-list{font-size:13.3px;line-height:20px;margin-top:9px}
</style>
</head>
<body>
<svg width="0" height="0" style="position:absolute">
  <defs>
    <g id="truck" fill="#fff">
      <rect x="0" y="0" width="14" height="10" rx="1"/>
      <path d="M15 3h4l3 4v3h-7z"/>
      <circle cx="4" cy="11" r="2.2"/>
      <circle cx="17" cy="11" r="2.2"/>
    </g>
    <g id="box" fill="#fff">
      <rect x="0" y="0" width="12" height="10" rx="1"/>
    </g>
  </defs>
</svg>

<main class="flyer">
  <div class="abs header-band"></div>
  <h1 class="abs heading header-title">Core Services</h1>

  <!-- row one -->
  <div class="service" style="left:93px;top:174px">
    <div class="service-icon"><svg viewBox="0 0 40 40"><path fill="#fff" d="M6 8l4 0 6 4 12 0c3 0 3 3 0 3l-10 0-5 4-3 0 2-4-4 0z"/><use href="#truck" x="8" y="22"/></svg></div>
    <div class="service-label">STAT/ASAP</div>
  </div>
  <div class="service" style="left:253px;top:174px">
    <div class="service-icon"><svg viewBox="0 0 40 40"><circle cx="22" cy="11" r="5" fill="none" stroke="#fff" stroke-width="2.5" stroke-dasharray="3 1.5"/><use href="#truck" x="7" y="20" transform="scale(1.15) translate(-3 -3)"/></svg></div>
    <div class="service-label">Same Day</div>
  </div>
  <div class="service" style="left:408px;top:174px">
    <div class="service-icon"><svg viewBox="0 0 40 40"><circle cx="20" cy="20" r="14" fill="none" stroke="#fff" stroke-width="2.5" stroke-dasharray="34 10"/><rect x="13" y="14" width="14" height="12" fill="none" stroke="#fff" stroke-width="2.5"/></svg></div>
    <div class="service-label">Next Day</div>
  </div>
  <div class="service" style="left:560px;top:174px">
    <div class="service-icon"><svg viewBox="0 0 40 40"><path d="M9 22v-4a11 11 0 0 1 22 0v4" fill="none" stroke="#fff" stroke-width="2.5"/><rect x="6" y="19" width="6" height="9" rx="2" fill="#fff"/><rect x="28" y="19" width="6" height="9" rx="2" fill="#fff"/><path d="M31 28c0 4-4 6-8 6" fill="none" stroke="#fff" stroke-width="2"/><rect x="15" y="16" width="10" height="9" fill="#fff"/></svg></div>
    <div class="service-label">Scheduled</div>
  </div>
  <div class="service" style="left:733px;top:174px">
    <div class="service-icon"><svg viewBox="0 0 40 40"><path d="M8 8h22M30 8v6H10v5" fill="none" stroke="#fff" stroke-width="2.5"/><circle cx="8" cy="8" r="3" fill="#fff"/><circle cx="30" cy="8" r="3" fill="#fff"/><use href="#truck" x="8" y="22"/></svg></div>
    <div class="service-label">Extended Drives</div>
  </div>
  <div class="divider" style="left:175px;top:171px;height:94px"></div>
  <div class="divider" style="left:331px;top:171px;height:94px"></div>
  <div class="divider" style="left:479px;top:171px;height:94px"></div>
  <div class="divider" style="left:632px;top:171px;height:94px"></div>

  <!-- row two -->
  <div class="service" style="left:162px;top:302px">
    <div class="service-icon"><svg viewBox="0 0 40 40"><use href="#box" x="14" y="6"/><use href="#box" x="7" y="20"/><use href="#box" x="21" y="20"/></svg></div>
    <div class="service-label">Onboard Courier</div>
  </div>
  <div class="service" style="left:371px;top:300px">
    <div class="service-icon"><svg viewBox="0 0 40 40"><rect x="13" y="13" width="14" height="14" fill="#fff"/><path d="M6 6l5 5M34 6l-5 5M6 34l5-5M34 34l-5-5" stroke="#fff" stroke-width="2.5"/></svg></div>
    <div class="service-label" style="margin-top:10px">Reverse Logistics</div>
  </div>
  <div class="service" style="left:549px;top:304px">
    <div class="service-icon"><svg viewBox="0 0 40 40"><rect x="19" y="7" width="14" height="12" fill="#fff"/><path d="M11 6v10M7 12l4 4 4-4" fill="none" stroke="#fff" stroke-width="2.5"/><path d="M6 24h4l6 4h8l8-4c2 0 2 3 0 4l-8 5H8z" fill="#fff"/></svg></div>
    <div class="service-label">White Glove</div>
  </div>
  <div class="service" style="left:702px;top:303px">
    <div class="service-icon"><svg viewBox="0 0 40 40"><use href="#box" x="6" y="7"/><use href="#box" x="22" y="7"/><use href="#box" x="6" y="23"/><use href="#box" x="22" y="23"/></svg></div>
    <div class="service-label">Warehousing</div>
  </div>
  <div class="divider" style="left:262px;top:300px;height:94px"></div>
  <div class="divider" style="left:472px;top:300px;height:94px"></div>
  <div class="divider" style="left:624px;top:300px;height:94px"></div>

  <!-- industries -->
  <h2 class="abs heading industries-pill">Industries Served</h2>
  <ul class="industry-list" style="left:52px;top:512px">
    <li>Healthcare &amp; Life Sciences</li>
    <li>Pharmaceuticals</li>
    <li>Retailers &amp; E-Commerce</li>
    <li>Distributors &amp; Manufacturers</li>
    <li>Educational Institutions</li>
  </ul>
  <div class="divider" style="left:423px;top:515px;height:178px"></div>
  <ul class="industry-list" style="left:497px;top:512px">
    <li>Legal &amp; Financial Services</li>
    <li>Food &amp; Beverage</li>
    <li>Technology &amp; IT Companies</li>
    <li>Government &amp; Defense<br>Companies</li>
  </ul>

  <!-- technology -->
  <div class="abs tech-band"></div>
  <h2 class="abs heading tech-title">Technology Highlights</h2>
  <ul class="tech-list">
    <li>Advanced Integration Capabilities</li>
    <li>GPS Tracking</li>
    <li>Live Vehicle Monitoring</li>
    <li>Client Online Portal</li>
    <li style="margin-top:16px">Emphasis on Real-Time Tracking<br>and seamless integrations</li>
  </ul>

  <section class="abs fleet-card">
    <h3 class="heading fleet-title">Fleet Capabilities</h3>
    <p class="fleet-text">Variety of Vehicles: Sedans, SUVs,<br>Pickup Trucks, Cargo Vans, Sprinters,<br>Straight Trucks</p>
    <h3 class="heading fleet-title second">Key Vehicle Features</h3>
    <p class="fleet-text liftgate">Liftgate capabilities prominently noted</p>
  </section>

  <!-- hubs -->
  <section class="abs hub-band">
    <h2 class="heading hub-title">Hub Locations</h2>
    <p class="hub-list">Fargo, ND | Bismarck, ND | Devils Lake, ND | Grand Forks, ND</p>
    <h2 class="heading airport-title">Airport Codes Serviced</h2>
    <p class="airport-list">FAR - Fargo, ND | BIS - Bismarck, ND | MOT - Minot, ND | GFK - Grand Forks, ND | XWA - Williston, ND | DIK - Dickinson, ND<br>
    DVL - Devils Lake, ND | JMS - Jamestown, ND | ABR - Aberdeen, SD | ATY - Watertown, SD | TRF - Thief River Falls, MN<br>
    BJI - Bemidji, MN | DTL - Detroit Lakes, MN | MSP - Minneapolis/St. Paul, MN</p>
  </section>
</main>
</body>
</html>
```